Leadership Training Business Needs a business card design

We need a business card designed for our company based in Auckland, New Zealand called Crestfield Guidance Services. We conduct a variety of residential programmes that provide for differnet management levels. These programmes are designed to familiarise managers with important leadership concepts and techniques. This learning is reinforced through the provision of real workplace feedback and the use of action learning opportunities (experiential exercises) to develop the participants' leadership skills and potential. We would like to add our tag line which is:
Inspires Direction - Instils Values - Delivers Results
We would like the card to be a white background but would consider a different background colour on the back. Possibly include the following words on the back:
- Organisational Development
- Positive Cultural Change
- Leadership Programmes
- Practical Development "Tools"
- Crew Balance Inventory
- 360o degree Assessments
- Strengths Based Training
- Coaching and Mentoring

Industry/Entity Type

Business

Requirements
Must have
• Company Name, logo, contact details, website address and email.
• Persons name and their title

```html
<!DOCTYPE html>
<html lang="en">
<head>
<meta charset="utf-8">
<title>Crestfield Guidance Services – Business Card</title>
<link rel="stylesheet" href="https://fonts.googleapis.com/css2?family=Titillium+Web:ital,wght@0,400;0,600;0,700;1,600&display=swap">
<style>
  :root {
    --stage: #3a3a3c;
    --brand-blue: #3049a0;
    --ink-blue: #2f3f98;
    --paper: #ffffff;
    --tick: #f2d21f;
    --grad-green: #8cc63f;
    --grad-yellow: #f4e423;
    --grad-orange: #f7941d;
    --font-main: "Titillium Web", sans-serif;
  }
  * { box-sizing: border-box; margin: 0; padding: 0; }
  html, body { width: 1200px; height: 800px; overflow: hidden; }
  body {
    background: var(--stage);
    font-family: var(--font-main);
    position: relative;
  }
  .card {
    position: absolute;
    top: 100px;
    width: 340px;
    height: 600px;
    padding: 40px 32px 36px;
    display: flex;
    flex-direction: column;
    box-shadow: 0 12px 30px rgba(0,0,0,.45);
  }
  .card--back { left: 240px; background: var(--brand-blue); color: var(--paper); }
  .card--front { left: 620px; background: var(--paper); color: var(--ink-blue); }

  .brand { text-align: center; }
  .brand__mark {
    width: 86px; height: 86px; border-radius: 50%;
    background: var(--grad-orange);
    margin: 0 auto 18px;
  }
  .brand__name { font-weight: 600; font-size: 24px; line-height: 1.1; }
  .brand__sub  { font-weight: 600; font-size: 24px; line-height: 1.1; }
  .brand__tagline { font-style: italic; font-weight: 600; font-size: 12.5px; margin-top: 6px; }

  .card--front .brand__mark { width: 70px; height: 70px; margin-bottom: 14px; }
  .card--front .brand__name,
  .card--front .brand__sub { font-weight: 400; font-size: 19px; }

  .grad-bar {
    height: 14px;
    background: linear-gradient(90deg, var(--grad-green), var(--grad-yellow) 50%, var(--grad-orange));
  }

  .services { list-style: none; margin: 44px auto 0; }
  .services li {
    display: flex; align-items: center; gap: 8px;
    font-size: 17px; font-weight: 600; line-height: 1.55;
  }
  .services svg { width: 14px; height: 14px; flex: none; }
  .card--back .grad-bar { margin-top: auto; }

  .card--front .brand .grad-bar { margin: 12px 10px 0; }
  .person { text-align: center; margin-top: 20px; }
  .person__name { font-weight: 700; font-size: 20px; letter-spacing: .5px; }
  .person__title { font-weight: 600; font-size: 17px; line-height: 1; }
  .contact { margin-top: auto; text-align: center; font-size: 14.5px; font-weight: 600; line-height: 1.6; }
  .card--front > .grad-bar { margin: 14px 10px 0; }
</style>
</head>
<body>

<section class="card card--back" aria-label="Card back">
  <div class="brand">
    <div class="brand__mark"></div>
    <p class="brand__name">Crestfield Guidance Services</p>
    <p class="brand__sub">Leadership Programmes</p>
    <p class="brand__tagline">Inspires Direction - Instils Values - Delivers Results</p>
  </div>

  <ul class="services">
    <li><svg viewBox="0 0 14 14"><path d="M1 7l4 4 8-10" fill="none" stroke="var(--tick)" stroke-width="2.6" stroke-linecap="round" stroke-linejoin="round"/></svg>Organisational Development</li>
    <li><svg viewBox="0 0 14 14"><path d="M1 7l4 4 8-10" fill="none" stroke="var(--tick)" stroke-width="2.6" stroke-linecap="round" stroke-linejoin="round"/></svg>Positive Cultural Change</li>
    <li><svg viewBox="0 0 14 14"><path d="M1 7l4 4 8-10" fill="none" stroke="var(--tick)" stroke-width="2.6" stroke-linecap="round" stroke-linejoin="round"/></svg>Leadership Programmes</li>
    <li><svg viewBox="0 0 14 14"><path d="M1 7l4 4 8-10" fill="none" stroke="var(--tick)" stroke-width="2.6" stroke-linecap="round" stroke-linejoin="round"/></svg>Practical Development Tools</li>
    <li><svg viewBox="0 0 14 14"><path d="M1 7l4 4 8-10" fill="none" stroke="var(--tick)" stroke-width="2.6" stroke-linecap="round" stroke-linejoin="round"/></svg>Crew Balance Inventory</li>
    <li><svg viewBox="0 0 14 14"><path d="M1 7l4 4 8-10" fill="none" stroke="var(--tick)" stroke-width="2.6" stroke-linecap="round" stroke-linejoin="round"/></svg>360 Degree Assessments</li>
    <li><svg viewBox="0 0 14 14"><path d="M1 7l4 4 8-10" fill="none" stroke="var(--tick)" stroke-width="2.6" stroke-linecap="round" stroke-linejoin="round"/></svg>Strengths Based Training</li>
    <li><svg viewBox="0 0 14 14"><path d="M1 7l4 4 8-10" fill="none" stroke="var(--tick)" stroke-width="2.6" stroke-linecap="round" stroke-linejoin="round"/></svg>Coaching and Mentoring</li>
  </ul>

  <div class="grad-bar"></div>
</section>

<section class="card card--front" aria-label="Card front">
  <div class="brand">
    <div class="brand__mark"></div>
    <p class="brand__name">Crestfield Guidance Services</p>
    <p class="brand__sub">Leadership Programmes</p>
    <div class="grad-bar"></div>
  </div>

  <div class="person">
    <p class="person__name">DANIEL ASHCOMBE</p>
    <p class="person__title">Facilitator</p>
  </div>

  <div class="contact">
    <p>Telephone: 12 48 3091</p>
    <p>Email: daniel@crestfieldgs.co.nz</p>
    <p>Website: www.crestfieldgs.co.nz</p>
  </div>

  <div class="grad-bar"></div>
</section>

</body>
</html>
```